Design logo and business card.

Design and construct logo and card for my business which is an over seeing company of other smaller businesses. The companies name is eleven5 venture alliance. Im open to any ideas but i am looking for a very cool contemporary design with a very prestige feel. The card can be either single or double sided, Thank you and i will look forward to your submissions.

Industry/Entity Type

Business

Requirements
Must have
• Company name, email, website, telephone, my name. Cool modern look with a prestige feel.

```html
<!DOCTYPE html>
<html lang="en">
<head>
<meta charset="utf-8">
<title>eleven5 venture alliance — business card</title>
<link rel="stylesheet" href="https://fonts.googleapis.com/css2?family=Raleway:wght@200;300&display=swap">
<style>
  :root {
    --backdrop: #d9d9d9;
    --card: #0c0c0d;
    --card-tone: #1b1b1e;
    --ink: #f2f2f2;
    --ink-soft: #bfc3c7;
    --accent: #1aa3d6;
    --accent-glow: #6fd3ff;
    --icon-tile: #1f2a30;
  }
  html, body {
    margin: 0;
    width: 1200px;
    height: 1000px;
    overflow: hidden;
    background: var(--backdrop);
  }
  .canvas {
    position: relative;
    width: 1200px;
    height: 1000px;
    font-family: "Raleway", sans-serif;
  }
  .card {
    position: absolute;
    background: var(--card);
    box-shadow: 0 18px 40px rgba(0,0,0,0.35);
    overflow: hidden;
  }
  .card-pattern {
    position: absolute;
    inset: 0;
    background: radial-gradient(ellipse at 50% 45%, var(--card-tone) 0%, var(--card) 75%);
  }
  .card-front { left: 110px; top: 110px; width: 620px; height: 400px; }
  .card-back  { left: 490px; top: 478px; width: 560px; height: 360px; }

  .brand {
    position: absolute;
    display: flex;
    align-items: center;
    color: var(--ink);
    font-weight: 200;
    white-space: nowrap;
  }
  .brand-dot {
    flex: none;
    border-radius: 50%;
    background: var(--accent);
    box-shadow: 0 0 18px var(--accent-glow);
  }
  .card-front .brand { left: 150px; top: 168px; font-size: 34px; gap: 18px; }
  .card-front .brand-dot { width: 46px; height: 46px; }

  .card-back .brand { left: 62px; top: 156px; font-size: 17px; line-height: 1.2; gap: 10px; }
  .card-back .brand-dot { width: 24px; height: 24px; }
  .brand-line { display: block; }

  .contact {
    position: absolute;
    left: 238px;
    top: 112px;
    margin: 0;
    padding: 0;
    list-style: none;
  }
  .contact-item {
    display: flex;
    align-items: center;
    gap: 12px;
    height: 34px;
    color: var(--ink-soft);
    font-weight: 300;
    font-size: 22px;
    letter-spacing: 0.2px;
    white-space: nowrap;
  }
  .contact-icon {
    width: 24px;
    height: 24px;
    flex: none;
  }
</style>
</head>
<body>
<main class="canvas">

  <section class="card card-front" aria-label="Card front">
    <div class="card-pattern" role="img" aria-label="Dark tone-on-tone floral damask pattern"></div>
    <div class="brand">
      <span class="brand-dot"></span>
      <span class="brand-name">eleven5 venture alliance</span>
    </div>
  </section>

  <section class="card card-back" aria-label="Card back">
    <div class="card-pattern" role="img" aria-label="Dark tone-on-tone floral damask pattern"></div>
    <div class="brand">
      <span class="brand-dot"></span>
      <span class="brand-name">
        <span class="brand-line">eleven5</span>
        <span class="brand-line">venture alliance</span>
      </span>
    </div>
    <ul class="contact">
      <li class="contact-item">
        <svg class="contact-icon" viewBox="0 0 24 24" aria-hidden="true">
          <rect width="24" height="24" rx="3" fill="var(--icon-tile)"/>
          <circle cx="12" cy="9" r="4" fill="#e6e6e6"/>
          <path d="M4 22c0-5 3.5-7 8-7s8 2 8 7z" fill="#e6e6e6"/>
        </svg>
        <span>kai lorne</span>
      </li>
      <li class="contact-item">
        <svg class="contact-icon" viewBox="0 0 24 24" aria-hidden="true">
          <rect width="24" height="24" rx="3" fill="var(--icon-tile)"/>
          <circle cx="12" cy="12" r="8" fill="none" stroke="#e6e6e6" stroke-width="1.4"/>
          <ellipse cx="12" cy="12" rx="3.5" ry="8" fill="none" stroke="#e6e6e6" stroke-width="1.2"/>
          <line x1="4" y1="12" x2="20" y2="12" stroke="#e6e6e6" stroke-width="1.2"/>
        </svg>
        <span>eleven5-alliance.com</span>
      </li>
      <li class="contact-item">
        <svg class="contact-icon" viewBox="0 0 24 24" aria-hidden="true">
          <rect width="24" height="24" rx="3" fill="var(--icon-tile)"/>
          <rect x="4" y="7" width="16" height="11" fill="#e6e6e6"/>
          <path d="M4 7l8 6 8-6" fill="none" stroke="#7a8a94" stroke-width="1.2"/>
        </svg>
        <span>info@eleven5-alliance.com</span>
      </li>
      <li class="contact-item">
        <svg class="contact-icon" viewBox="0 0 24 24" aria-hidden="true">
          <rect width="24" height="24" rx="3" fill="var(--icon-tile)"/>
          <path d="M7 5h3l1 4-2 1.5a9 9 0 0 0 4.5 4.5L15 13l4 1v3a2 2 0 0 1-2 2A12 12 0 0 1 5 7a2 2 0 0 1 2-2z" fill="#e6e6e6"/>
        </svg>
        <span>+34 611 402 958</span>
      </li>
    </ul>
  </section>

</main>
</body>
</html>
```